Northfield Builders Guild Business card

We are looking for a new business card design with photo included.
Our business is a nonprofit construction contractor membership organization. We offer business education, assist with business setup and licensing, provide safety training, and provide a member directory.
URL: www.brickwayguildnetwork.org
Color code:
CMYK: 0 cyan, 42 magenta, 100 yellow, 0 black for Print.
Hexidecimal: #FF9900
RGB: R 255; G 153; B 0

```html
<!DOCTYPE html>
<html lang="en">
<head>
<meta charset="utf-8">
<title>Northfield Builders Guild – Business Card</title>
<link href="https://fonts.googleapis.com/css2?family=Source+Sans+3:wght@400;700;900&display=swap" rel="stylesheet">
<style>
  :root {
    --backdrop: #cdcdcd;
    --charcoal: #3d3b3c;
    --charcoal-deep: #353334;
    --amber: #ff9900;
    --amber-card: #eba526;
    --paper: #ffffff;
    --ink: #3d3b3c;
  }
  * { margin: 0; padding: 0; box-sizing: border-box; }
  html, body {
    width: 1200px; height: 800px; overflow: hidden;
    background: var(--backdrop);
    font-family: "Source Sans 3", "Source Sans Pro", sans-serif;
  }
  .canvas { position: relative; width: 1200px; height: 800px; }
  .card {
    position: absolute; left: 320px; width: 560px; height: 320px;
    overflow: hidden; box-shadow: 0 6px 18px rgba(0,0,0,.18);
  }
  .card--back { top: 56px; background: linear-gradient(135deg, var(--charcoal), var(--charcoal-deep)); }
  .card--front { top: 424px; background: var(--paper); }

  .brand { position: absolute; display: flex; align-items: center; gap: 10px; }
  .brand__mark { width: 14px; height: 14px; background: var(--amber); flex: none; }
  .brand__name {
    font-weight: 900; font-size: 25px; line-height: 1.02;
    text-transform: uppercase; letter-spacing: -.3px;
  }
  .card--back .brand { left: 58px; top: 124px; }
  .card--back .brand__name { color: var(--paper); }

  .divider { position: absolute; left: 300px; top: 108px; width: 2px; height: 104px; background: var(--amber); }
  .services { position: absolute; left: 322px; top: 112px; list-style: none; color: var(--paper); font-size: 15px; line-height: 24px; text-transform: uppercase; }
  .services li::before { content: "•"; color: var(--amber); margin-right: 6px; }

  .card-shapes { position: absolute; inset: 0; }
  .card--front .brand { left: 352px; top: 66px; }
  .card--front .brand__name { color: var(--ink); font-size: 22px; }

  .holder { position: absolute; left: 34px; top: 74px; color: var(--paper); }
  .holder__name { font-weight: 700; font-size: 22px; letter-spacing: .5px; text-transform: uppercase; }
  .holder__role { font-size: 16px; margin-top: 2px; }

  .contact { position: absolute; left: 34px; top: 196px; color: var(--paper); font-size: 14px; line-height: 19px; list-style: none; }
  .contact li { display: flex; align-items: center; gap: 7px; }
  .contact .address { margin-left: 0; }
  .contact svg { width: 12px; height: 12px; flex: none; }
</style>
</head>
<body>
<main class="canvas">

  <section class="card card--back" aria-label="Card back">
    <div class="brand">
      <span class="brand__mark"></span>
      <span class="brand__name">Northfield<br>Builders Guild</span>
    </div>
    <span class="divider"></span>
    <ul class="services">
      <li>Technical Assistance</li>
      <li>Contractor Education</li>
      <li>Safety &amp; Compliance</li>
      <li>Contractor Directory</li>
    </ul>
  </section>

  <section class="card card--front" aria-label="Card front">
    <svg class="card-shapes" viewBox="0 0 560 320" preserveAspectRatio="none" aria-hidden="true">
      <polygon points="0,0 312,0 336,152 0,180" fill="var(--amber-card)"/>
      <polygon points="0,186 338,158 560,206 560,320 0,320" fill="var(--charcoal)"/>
    </svg>

    <div class="brand">
      <span class="brand__mark"></span>
      <span class="brand__name">Northfield<br>Builders Guild</span>
    </div>

    <div class="holder">
      <p class="holder__name">Daniel Harper</p>
      <p class="holder__role">President</p>
    </div>

    <ul class="contact">
      <li class="address">2450 NW Alder Ridge Rd., Suite #210</li>
      <li class="address">Salem, OR 97304</li>
      <li>
        <svg viewBox="0 0 12 12"><path d="M3 1l2 2.5-1.2 1.2a7 7 0 0 0 3.5 3.5L8.5 7 11 9l-1.2 2C5 11 1 7 1 2.2z" fill="var(--amber)"/></svg>
        (555) 214-7730
      </li>
      <li>
        <svg viewBox="0 0 12 12"><rect x="3" y="1" width="6" height="4" fill="var(--amber)"/><rect x="1" y="5" width="10" height="6" rx="1" fill="var(--amber)"/></svg>
        555.318.0462
      </li>
      <li>
        <svg viewBox="0 0 12 12"><rect x="1" y="2.5" width="10" height="7" fill="none" stroke="var(--amber)" stroke-width="1.4"/><path d="M1 2.5l5 4 5-4" fill="none" stroke="var(--amber)" stroke-width="1.4"/></svg>
        daniel@brickwayguildnetwork.org
      </li>
      <li>
        <svg viewBox="0 0 12 12"><circle cx="6" cy="6" r="5" fill="none" stroke="var(--amber)" stroke-width="1.3"/><path d="M1 6h10M6 1c-2.5 3-2.5 7 0 10M6 1c2.5 3 2.5 7 0 10" fill="none" stroke="var(--amber)" stroke-width="1"/></svg>
        www.brickwayguildnetwork.org
      </li>
    </ul>
  </section>

</main>
</body>
</html>
```